Hollyfen and Loam Website Refresh

Please take a look at how bad our current site looks. www.hollyfenandloam.co.uk

We would like to use www.pagloft.com to rebuild our Ecommerce offering. PLease take a look at the available templates for eCommerce stores on www.pagloft.com and get designing. We want a simple, fresh look without too much content and clutter.

We would welcome a new logo (or at least a fresh look of the current one) and font for the company to so be creative! Whites and Earthy greens are preferable but again we are happy to see other options.

Ultimately the core focus of the business is pots and glass wear for the home. Although we do tend to find other products from time to time.

We are about english heritage.

```html
<!DOCTYPE html>
<html lang="en">
<head>
<meta charset="utf-8">
<title>Hollyfen and Loam</title>
<link rel="stylesheet" href="https://fonts.googleapis.com/css2?family=Lobster&family=Open+Sans:ital,wght@0,400;0,600;0,700;1,400&display=swap">
<style>
:root{
  --moss:#5d6b38;
  --moss-dark:#4a5a2c;
  --loam:#7a5a3c;
  --ink:#4a4a4a;
  --muted:#8a8a8a;
  --icon:#555555;
  --nav-icon:#aaaaaa;
  --band:#eef0ea;
  --card:#f5f6f2;
  --white:#ffffff;
}
*{box-sizing:border-box;margin:0;padding:0}
html,body{width:868px;height:1200px;overflow:hidden;background:var(--white)}
body{position:relative;font-family:"Open Sans",Arial,sans-serif;color:var(--ink)}

.site-header{position:absolute;left:0;top:0;width:868px;height:92px;background:var(--white);box-shadow:0 1px 3px rgba(0,0,0,.06)}
.brand{position:absolute;left:91px;top:30px;display:flex;align-items:center;gap:8px}
.brand-dot{width:16px;height:16px;border-radius:50%;background:var(--moss)}
.brand-name{font-weight:600;font-size:20px;color:var(--moss);letter-spacing:.2px}
.main-nav{position:absolute;left:377px;top:0;display:flex;height:73px}
.nav-item{display:flex;flex-direction:column;align-items:center;justify-content:flex-end;padding-bottom:9px;font-size:11px;color:#666;text-transform:uppercase;height:73px}
.nav-item svg{margin-bottom:11px}
.nav-item.is-active{background:var(--moss);color:var(--white);width:64px}
.nav-terms{width:70px}
.nav-faq{width:50px}
.nav-service{width:76px}
.nav-about{width:62px}
.nav-contact{width:84px}

.hero{position:absolute;left:0;top:92px;width:868px;height:415px;background:var(--band)}
.slider{position:absolute;left:134px;top:116px;width:603px;height:363px;background:var(--white);box-shadow:0 1px 4px rgba(0,0,0,.15)}
.slide{position:absolute;left:3px;top:4px;width:597px;height:280px;background:linear-gradient(180deg,#6f8f5a 0%,#4f7a36 40%,#3f5e2c 70%,#6d5a46 100%)}
.caption{position:absolute;left:10px;top:202px;width:566px;height:64px;background:rgba(40,40,30,.6);padding:6px 14px;color:var(--white);font-size:10.5px;font-style:italic;line-height:18px}
.arrow{position:absolute;top:161px;width:46px;height:46px;background:var(--moss);display:flex;align-items:center;justify-content:center}
.arrow-prev{left:12px}
.arrow-next{left:539px}
.thumbs{position:absolute;left:3px;top:289px;display:flex;gap:1px}
.thumb{width:149px;height:70px}
.thumb-1{background:linear-gradient(180deg,#5d8a3e,#7b6a52)}
.thumb-2{background:linear-gradient(180deg,#9aa08e,#7c7a6c)}
.thumb-3{background:linear-gradient(180deg,#5b6a4c,#cfcfcf)}
.thumb-4{background:linear-gradient(180deg,#7da35a,#8d5a3b)}

.intro{position:absolute;left:0;top:538px;width:868px;text-align:center}
.intro-title{font-family:"Lobster",cursive;font-weight:400;font-size:24px;line-height:32px;color:var(--ink)}
.intro-title em{font-style:normal;color:var(--moss)}
.intro-sub{margin-top:4px;font-size:13px;font-style:italic;color:var(--muted)}

.features{position:absolute;left:72px;top:637px;display:flex;gap:15px}
.feature{width:170px;height:201px;background:var(--card);border-bottom:2px solid var(--moss);text-align:center;padding-top:16px}
.feature-icon{height:34px;display:flex;align-items:center;justify-content:center}
.feature h3{margin-top:12px;font-size:11px;font-weight:600;color:#444;letter-spacing:.2px}
.feature p{margin:7px auto 0;width:150px;height:74px;font-size:9.5px;line-height:18.5px;color:var(--muted)}
.btn{display:inline-block;margin-top:4px;width:78px;height:20px;line-height:20px;background:var(--moss);color:var(--white);font-size:9.5px;font-style:italic}

.section-rule{position:absolute;left:72px;top:869px;width:724px;border-top:1px dotted #cfcfcf}
.section-title{position:absolute;left:0;top:856px;width:868px;text-align:center;font-weight:400}
.section-title span{background:var(--white);padding:0 20px;font-family:"Lobster",cursive;font-size:18px;color:var(--ink)}

.products{position:absolute;left:72px;top:915px;display:flex;gap:15px}
.product{width:170px;height:268px;background:var(--card);border-bottom:2px solid var(--moss);text-align:center}
.product-photo{margin:0 auto;width:127px;height:184px}
.photo-bowl{background:linear-gradient(180deg,#e9e4da 0%,#a7a25a 40%,#6b4a3c 80%,#e2ddd3 100%)}
.photo-pot{background:linear-gradient(180deg,#8e8a80 0%,#9cb36a 30%,#8aa45a 80%,#5a3f2e 100%)}
.photo-bag{width:110px;background:linear-gradient(180deg,#7e8f6a 0%,#6a7f5a 40%,#7a3a40 60%,#8fa078 100%)}
.photo-birdhouse{width:134px;background:linear-gradient(180deg,#8a8d8e 0%,#9a8a6a 50%,#7e7262 100%)}
.price{margin-top:17px;font-size:11px;font-weight:600;color:#555}
.actions{margin-top:10px;display:flex;justify-content:center;gap:8px}
.round{width:28px;height:28px;border-radius:50%;background:var(--moss);display:flex;align-items:center;justify-content:center}
</style>
</head>
<body>
<header class="site-header">
  <div class="brand"><span class="brand-dot"></span><span class="brand-name">Hollyfen and Loam</span></div>
  <nav class="main-nav">
    <div class="nav-item is-active"><svg width="10" height="9" viewBox="0 0 10 9"><path d="M5 0L0 4.5h1.5V9h2.5V6h2v3h2.5V4.5H10z" fill="#fff"/></svg>Home</div>
    <div class="nav-item nav-terms"><svg width="11" height="8" viewBox="0 0 11 8"><rect x="0" y="1.5" width="11" height="6.5" rx="1" fill="#aaa"/><rect x="3.5" y="0" width="4" height="2" fill="#aaa"/><circle cx="5.5" cy="4.7" r="1.8" fill="#fff"/></svg>Terms</div>
    <div class="nav-item nav-faq"><svg width="11" height="9" viewBox="0 0 11 9"><ellipse cx="5.5" cy="4" rx="5.5" ry="3.8" fill="#aaa"/><path d="M2 6l-1 3 3-2z" fill="#aaa"/></svg>FAQ</div>
    <div class="nav-item nav-service"><svg width="11" height="9" viewBox="0 0 11 9"><rect y="0" width="11" height="2" fill="#aaa"/><rect y="3.5" width="11" height="2" fill="#aaa"/><rect y="7" width="11" height="2" fill="#aaa"/></svg>Service</div>
    <div class="nav-item nav-about"><svg width="9" height="9" viewBox="0 0 9 9"><circle cx="4.5" cy="2.3" r="2.3" fill="#aaa"/><path d="M0 9c0-3 2-4.3 4.5-4.3S9 6 9 9z" fill="#aaa"/></svg>About</div>
    <div class="nav-item nav-contact"><svg width="11" height="8" viewBox="0 0 11 8"><rect width="11" height="8" fill="#aaa"/><path d="M0 0l5.5 4.5L11 0" stroke="#fff" fill="none"/></svg>Contact</div>
  </nav>
</header>

<section class="hero"></section>
<div class="slider">
  <div class="slide" role="img" aria-label="Raised timber and metal planter beds full of green shrubs in front of a dark garden shed">
    <div class="caption">Weathered terracotta, hand-thrown pots and old English glassware, gathered from potteries and country sales across the shires. Every piece is chosen to bring a little heritage charm to your home, your kitchen and your garden.</div>
    <div class="arrow arrow-prev"><svg width="8" height="12" viewBox="0 0 8 12"><rect x="0" y="5" width="3" height="3" fill="#fff"/><rect x="4" y="0" width="3" height="3" fill="#fff"/><rect x="4" y="9" width="3" height="3" fill="#fff"/></svg></div>
    <div class="arrow arrow-next"><svg width="8" height="12" viewBox="0 0 8 12"><rect x="5" y="5" width="3" height="3" fill="#fff"/><rect x="1" y="0" width="3" height="3" fill="#fff"/><rect x="1" y="9" width="3" height="3" fill="#fff"/></svg></div>
  </div>
  <div class="thumbs">
    <div class="thumb thumb-1" role="img" aria-label="Raised planter beds with shrubs"></div>
    <div class="thumb thumb-2" role="img" aria-label="Community garden beds with visitors"></div>
    <div class="thumb thumb-3" role="img" aria-label="Stone trough planter with flowers"></div>
    <div class="thumb thumb-4" role="img" aria-label="Gardener tending a timber raised bed"></div>
  </div>
</div>

<section class="intro">
  <h1 class="intro-title">We are <em>Hollyfen and Loam</em>, pots and glassware for the English home.</h1>
  <p class="intro-sub">Hand-picked pots, glassware and garden finds. A little English heritage for every home.</p>
</section>

<section class="features">
  <article class="feature">
    <div class="feature-icon"><svg width="34" height="32" viewBox="0 0 34 32"><rect x="3" y="2" width="28" height="6" fill="var(--icon)"/><path d="M6 10h22l-3 21H9z" fill="var(--icon)"/></svg></div>
    <h3>GARDEN POTS</h3>
    <p>Terracotta and glazed pots in earthy tones, made to weather well on any English terrace.</p>
    <span class="btn">Read more</span>
  </article>
  <article class="feature">
    <div class="feature-icon"><svg width="24" height="32" viewBox="0 0 24 32"><path d="M2 1h20c0 9-4 14-8.5 15v11H19v3H5v-3h5.5V16C6 15 2 10 2 1z" fill="var(--icon)"/></svg></div>
    <h3>GLASSWARE</h3>
    <p>Classic tumblers, jugs and vases for the table, with the feel of a country kitchen.</p>
    <span class="btn">Read more</span>
  </article>
  <article class="feature">
    <div class="feature-icon"><svg width="34" height="30" viewBox="0 0 34 30"><path d="M17 1L1 14h4v15h9v-9h6v9h9V14h4z" fill="var(--icon)"/></svg></div>
    <h3>HOME FINDS</h3>
    <p>Bird houses, bowls and bags we come across along the way, each one a small treasure.</p>
    <span class="btn">Read more</span>
  </article>
  <article class="feature">
    <div class="feature-icon"><svg width="34" height="32" viewBox="0 0 34 32"><path d="M17 1l4.7 10 10.8 1.2-8 7.4 2.2 10.7L17 24.8l-9.7 5.5 2.2-10.7-8-7.4L12.3 11z" fill="var(--icon)"/></svg></div>
    <h3>ENGLISH HERITAGE</h3>
    <p>Pieces with a story, chosen from English makers and crafts that have stood the test of time.</p>
    <span class="btn">Read more</span>
  </article>
</section>

<div class="section-rule"></div>
<h2 class="section-title"><span>Our Latest Finds</span></h2>

<section class="products">
  <article class="product">
    <div class="product-photo photo-bowl" role="img" aria-label="Bronze footed bowl filled with grapes, bananas and a pineapple"></div>
    <p class="price">GBP 57,50</p>
    <div class="actions">
      <span class="round"><svg width="12" height="12" viewBox="0 0 12 12"><circle cx="5" cy="5" r="3.5" fill="none" stroke="#fff" stroke-width="2"/><path d="M7.5 7.5L11 11" stroke="#fff" stroke-width="2.4"/></svg></span>
      <span class="round"><svg width="12" height="12" viewBox="0 0 12 12"><path d="M5 7L7 5M4 5.5L2.5 7a2 2 0 003 3L7 8.5M8 6.5L9.5 5a2 2 0 00-3-3L5 3.5" stroke="#fff" stroke-width="1.6" fill="none"/></svg></span>
    </div>
  </article>
  <article class="product">
    <div class="product-photo photo-pot" role="img" aria-label="Tall green glazed flower pot with a round emblem"></div>
    <p class="price">GBP 11,50</p>
    <div class="actions">
      <span class="round"><svg width="12" height="12" viewBox="0 0 12 12"><circle cx="5" cy="5" r="3.5" fill="none" stroke="#fff" stroke-width="2"/><path d="M7.5 7.5L11 11" stroke="#fff" stroke-width="2.4"/></svg></span>
      <span class="round"><svg width="12" height="12" viewBox="0 0 12 12"><path d="M5 7L7 5M4 5.5L2.5 7a2 2 0 003 3L7 8.5M8 6.5L9.5 5a2 2 0 00-3-3L5 3.5" stroke="#fff" stroke-width="1.6" fill="none"/></svg></span>
    </div>
  </article>
  <article class="product">
    <div class="product-photo photo-bag" role="img" aria-label="Red and black garden tool bag hanging on a wire plant support"></div>
    <p class="price">GBP 9,50</p>
    <div class="actions">
      <span class="round"><svg width="12" height="12" viewBox="0 0 12 12"><circle cx="5" cy="5" r="3.5" fill="none" stroke="#fff" stroke-width="2"/><path d="M7.5 7.5L11 11" stroke="#fff" stroke-width="2.4"/></svg></span>
      <span class="round"><svg width="12" height="12" viewBox="0 0 12 12"><path d="M5 7L7 5M4 5.5L2.5 7a2 2 0 003 3L7 8.5M8 6.5L9.5 5a2 2 0 00-3-3L5 3.5" stroke="#fff" stroke-width="1.6" fill="none"/></svg></span>
    </div>
  </article>
  <article class="product">
    <div class="product-photo photo-birdhouse" role="img" aria-label="Ornate aged metal acorn-shaped bird house on a grey wall"></div>
    <p class="price">GBP 29,00</p>
    <div class="actions">
      <span class="round"><svg width="12" height="12" viewBox="0 0 12 12"><circle cx="5" cy="5" r="3.5" fill="none" stroke="#fff" stroke-width="2"/><path d="M7.5 7.5L11 11" stroke="#fff" stroke-width="2.4"/></svg></span>
      <span class="round"><svg width="12" height="12" viewBox="0 0 12 12"><path d="M5 7L7 5M4 5.5L2.5 7a2 2 0 003 3L7 8.5M8 6.5L9.5 5a2 2 0 00-3-3L5 3.5" stroke="#fff" stroke-width="1.6" fill="none"/></svg></span>
    </div>
  </article>
</section>
</body>
</html>
```